Real Estate Valuation Services

format
A5 portrait, look at the picture
Double-sided: Front = visual & emotional, Back = informative & structured.
goal
Highlight the free hedonic property valuation as the main offer.
Build trust by presenting the company as an exclusive, family-owned real estate firm with local roots in Meilen/ZH.
Communicate the USP “Everything from one source” clearly – from valuation to notary support and tax guidance.
Target audience
Homeowners in the Lake Zurich region considering selling their property.
Clients who value exclusivity, professionalism, and personal service.
Design style
Modern, clean, elegant – plenty of white space. Look at the website: https://brunnhofwohnen.ch/
Tone: Professional, trustworthy, exclusive – not like a mass-market flyer.
If possible, the text should be in German. Contact details must be included:
info@brunnhofwohnen.ch
+41 77 562 18 04
Target Market(s)
property owner
Industry/Entity Type
real estate
Look and feel

```html
<!DOCTYPE html>
<html lang="de">
<head>
<meta charset="UTF-8">
<title>Brunnhof Wohnen – Flyer Immobilienbewertung</title>
<link href="https://fonts.googleapis.com/css2?family=Montserrat:wght@400;500;600;700&family=Arimo:wght@400&display=swap" rel="stylesheet">
<style>
  :root{
    --green:#62a523;
    --green-dark:#4e8d1a;
    --green-soft:#e8f1dc;
    --ink:#444;
    --ink-strong:#3a3a3a;
    --white:#fff;
    --page:#fff;
    --line:#cfcfcf;
  }
  *{box-sizing:border-box;margin:0;padding:0}
  html,body{width:1200px;height:1200px;overflow:hidden;background:var(--page)}
  body{position:relative;font-family:'Montserrat',sans-serif;color:var(--ink)}

  .card{position:absolute;left:250px;width:708px;height:500px;overflow:hidden}

  /* Front */
  .front{top:79px}
  .front-photo{position:absolute;inset:0 0 51px 0;
    background:linear-gradient(180deg,#e9dfc9 0%,#ddd0b4 28%,#b8c8d6 42%,#7d97ad 52%,#6f8a6a 62%,#8c8a6e 76%,#b7a992 88%,#c9bca6 100%)}
  .front-brand{position:absolute;top:198px;left:0;right:0;text-align:center;color:var(--green)}
  .front-brand .name{display:block;font-weight:700;font-size:44px;line-height:1;letter-spacing:.5px}
  .front-brand .sub{display:block;font-weight:500;font-size:15px;letter-spacing:3px;margin-top:4px}
  .front-headline{position:absolute;top:317px;left:0;right:0;text-align:center;font-family:'Arimo',sans-serif;color:var(--white);font-size:21px;text-shadow:0 1px 3px rgba(0,0,0,.35)}
  .front-subline{position:absolute;top:349px;left:0;right:0;text-align:center;font-family:'Arimo',sans-serif;color:var(--white);font-size:11.5px;text-shadow:0 1px 3px rgba(0,0,0,.35)}
  .front-bar{position:absolute;left:0;right:0;bottom:0;height:51px;background:var(--green);color:var(--white);font-size:9.5px;display:flex;align-items:center;padding:0 34px 0 28px}
  .front-bar .offer{flex:1}
  .front-bar .contact span+span{margin-left:12px}

  /* Back */
  .back{top:629px;background:var(--green)}
  .back-photo{position:absolute;left:0;top:0;bottom:0;width:330px;
    background:linear-gradient(90deg,rgba(98,165,35,0) 60%,var(--green) 100%),
               linear-gradient(180deg,#c9dbe8 0%,#a9bccb 25%,#7c7a6c 45%,#4b4a40 70%,#3a3a30 100%)}
  .panel{position:absolute;left:301px;top:36px;width:377px;height:431px;background:var(--white)}
  .panel-brand{position:absolute;left:23px;top:22px;color:var(--green-dark);text-align:center}
  .panel-brand .name{display:block;font-weight:700;font-size:21px;line-height:1}
  .panel-brand .sub{display:block;font-weight:500;font-size:9px;letter-spacing:1px;margin-top:2px}
  .panel-title{position:absolute;left:27px;top:72px;font-weight:700;font-size:19.5px;line-height:24px;color:var(--green)}
  .panel-intro{position:absolute;left:27px;top:127px;font-size:10.5px;line-height:15.5px;width:300px}
  .services{position:absolute;left:27px;top:186px;width:243px;list-style:none}
  .services li{display:flex;align-items:center;gap:5px;height:22.5px;font-weight:600;font-size:12px;color:var(--ink-strong);border-bottom:1px solid var(--line)}
  .services li:last-child{border-bottom:none}
  .services svg{width:8px;height:8px;flex:none}
  .usp{position:absolute;left:0;right:0;top:282px;height:61px;background:var(--green-soft);padding:10px 27px 0;font-size:10.5px;line-height:15px}
  .cta{position:absolute;left:27px;top:353px;font-weight:700;font-size:12.5px;line-height:16px;color:var(--green)}
  .panel-contact{position:absolute;left:27px;top:398px;font-size:10.5px;color:var(--ink-strong)}
  .panel-contact b{font-weight:600}
  .panel-contact span+span{margin-left:22px}
</style>
</head>
<body>

<section class="card front">
  <div class="front-photo" role="img" aria-label="Überdachte Terrasse mit Lounge-Möbeln und Blick auf den Zürichsee"></div>
  <div class="front-brand">
    <span class="name">Brunnhof</span>
    <span class="sub">WOHNEN</span>
  </div>
  <p class="front-headline">Ihr lokaler Immobilienprofi in Meilen verwurzelt</p>
  <p class="front-subline">am Zürichsee unterwegs</p>
  <div class="front-bar">
    <span class="offer">Vereinbaren Sie noch heute Ihre kostenlose Bewertung</span>
    <span class="contact"><span>Tel: +41 77 562 18 04</span><span>Mail: info@brunnhofwohnen.ch</span></span>
  </div>
</section>

<section class="card back">
  <div class="back-photo" role="img" aria-label="Porträt einer Beraterin vor Seelandschaft mit Bergen"></div>
  <div class="panel">
    <div class="panel-brand">
      <span class="name">Brunnhof</span>
      <span class="sub">WOHNEN</span>
    </div>
    <h1 class="panel-title">Ihr exklusiver Immobilienpartner<br>in der Region Zürichsee</h1>
    <p class="panel-intro">Als familiengeführtes Unternehmen mit Wurzeln in Meilen bieten wir Ihnen persönliche Betreuung, Diskretion und höchste Professionalität.</p>
    <ul class="services">
      <li><svg viewBox="0 0 10 10"><path d="M1 5.5l2.5 2.5L9 2" fill="none" stroke="#62a523" stroke-width="1.6"/></svg>Immobilienbewertung</li>
      <li><svg viewBox="0 0 10 10"><path d="M1 5.5l2.5 2.5L9 2" fill="none" stroke="#62a523" stroke-width="1.6"/></svg>Verkaufsstrategie &amp; Vermarktung</li>
      <li><svg viewBox="0 0 10 10"><path d="M1 5.5l2.5 2.5L9 2" fill="none" stroke="#62a523" stroke-width="1.6"/></svg>Notariats &amp; Vertragsbegleitung</li>
      <li><svg viewBox="0 0 10 10"><path d="M1 5.5l2.5 2.5L9 2" fill="none" stroke="#62a523" stroke-width="1.6"/></svg>Steuerberatung</li>
    </ul>
    <p class="usp">Alles aus einer Hand – von der Bewertung über den<br>Verkauf bis zur steuerlichen Beratung.<br>Exklusiv, professionell und persönlich.</p>
    <p class="cta">Kontaktieren Sie uns für Ihre kostenlose<br>Immobilienbewertung.</p>
    <p class="panel-contact"><span><b>Tel:</b> +41 77 562 18 04</span><span><b>Mail:</b> info@brunnhofwohnen.ch</span></p>
  </div>
</section>

</body>
</html>
```